Marlow Crest Group (Real Estate and Investment)

A high end, clean design.
We are a real estate company with sales, asset management and investment divisions. We want to use a black and white scheme which is really high end feel. The back of the card can just be the logo (black background with the white writing) as we will probably emboss this when we print)

Target Market(s)

High level investors, high end houses for sale

Industry/Entity Type

Business

Contact Information for Business Card

Name, position, phone number and email address
Glen Varley, Managing Director, 0437259064 and glen@marlowcrest-example.com.au

Requirements
Must have
• Back of the card to be the black background with the white writing (as per the attached images). Would like the capacity to emboss the writing and logo

```html
<!DOCTYPE html>
<html lang="en">
<head>
<meta charset="UTF-8">
<title>Marlow Crest Group – Business Card</title>
<link rel="stylesheet" href="https://fonts.googleapis.com/css2?family=Open+Sans:wght@400;700&family=Raleway:wght@400&display=swap">
<style>
  :root {
    --backdrop: #c8c8ca;
    --card-black: #0f0f0f;
    --map-grey: #242424;
    --band-grey: #4a4a4a;
    --paper-white: #ffffff;
    --ink-black: #111111;
  }
  * { margin: 0; padding: 0; box-sizing: border-box; }
  html, body { width: 1200px; height: 1200px; overflow: hidden; }
  body {
    background: radial-gradient(circle at 50% 45%, #dcdcde 0%, var(--backdrop) 70%);
    position: relative;
    font-family: "Open Sans", sans-serif;
  }
  .card {
    position: absolute;
    width: 700px;
    height: 400px;
    border-radius: 26px;
    overflow: hidden;
    background: var(--card-black);
    box-shadow: 0 18px 30px rgba(0,0,0,0.28);
  }
  .card-back { left: 140px; top: 150px; }
  .card-front { left: 360px; top: 640px; }

  /* back side: brand on black */
  .world-map {
    position: absolute;
    left: 40px; top: 40px;
    width: 620px; height: 320px;
    background: radial-gradient(ellipse at 50% 45%, var(--map-grey) 0%, rgba(36,36,36,0.6) 55%, rgba(15,15,15,0) 75%);
  }
  .brand-lockup {
    position: absolute;
    left: 0; right: 0; top: 110px;
    display: flex;
    flex-direction: column;
    align-items: center;
    gap: 26px;
  }
  .brand-mark {
    width: 110px; height: 110px;
    border: 2px solid var(--paper-white);
    border-radius: 50%;
  }
  .brand-name {
    font-family: "Raleway", sans-serif;
    font-weight: 400;
    font-size: 38px;
    letter-spacing: 1px;
    color: var(--paper-white);
    white-space: nowrap;
  }

  /* front side: contact details */
  .card-front .front-shape { position: absolute; inset: 0; }
  .front-brand {
    position: absolute;
    left: 20px; top: 150px;
    width: 300px;
    display: flex;
    flex-direction: column;
    align-items: center;
    gap: 16px;
  }
  .front-brand .brand-mark {
    width: 90px; height: 90px;
    border-color: var(--ink-black);
  }
  .front-brand .brand-name {
    font-size: 20px;
    color: var(--ink-black);
  }
  .contact {
    position: absolute;
    left: 450px; top: 78px;
    color: var(--paper-white);
    font-size: 13px;
    line-height: 1.4;
    white-space: nowrap;
  }
  .contact-name { font-weight: 700; font-size: 20px; line-height: 1.15; }
  .contact-role { margin-bottom: 14px; }
  .contact-address { margin-bottom: 14px; }
  .contact-line { display: flex; align-items: center; gap: 8px; }
  .contact-line svg { width: 12px; height: 12px; flex: none; fill: var(--paper-white); }
</style>
</head>
<body>

<section class="card card-back">
  <div class="world-map" role="img" aria-label="Faint world map in dark grey behind the brand name"></div>
  <div class="brand-lockup">
    <div class="brand-mark"></div>
    <div class="brand-name">MARLOW CREST GROUP</div>
  </div>
</section>

<section class="card card-front">
  <svg class="front-shape" width="700" height="400" viewBox="0 0 700 400" aria-hidden="true">
    <rect width="700" height="400" fill="var(--card-black)"/>
    <circle cx="175" cy="330" r="260" fill="var(--band-grey)"/>
    <circle cx="160" cy="330" r="255" fill="var(--paper-white)"/>
  </svg>

  <div class="front-brand">
    <div class="brand-mark"></div>
    <div class="brand-name">MARLOW CREST GROUP</div>
  </div>

  <div class="contact">
    <div class="contact-name">Glen Varley</div>
    <div class="contact-role">Managing Director</div>
    <div class="contact-address">18 Harbour Lane, Mosman<br>P.O. Box 412, Mosman NSW</div>
    <div class="contact-line">
      <svg viewBox="0 0 24 24"><path d="M6.6 10.8a15.1 15.1 0 0 0 6.6 6.6l2.2-2.2a1 1 0 0 1 1-.25 11.4 11.4 0 0 0 3.6.6 1 1 0 0 1 1 1V20a1 1 0 0 1-1 1A17 17 0 0 1 3 4a1 1 0 0 1 1-1h3.5a1 1 0 0 1 1 1c0 1.25.2 2.45.6 3.6a1 1 0 0 1-.25 1z"/></svg>
      <span>0437259064</span>
    </div>
    <div class="contact-line">
      <svg viewBox="0 0 24 24"><path d="M2 5h20v14H2z M2 5l10 8 10-8" fill="none" stroke="#fff" stroke-width="2"/></svg>
      <span>glen@marlowcrest-example.com.au</span>
    </div>
    <div class="contact-line">
      <svg viewBox="0 0 24 24"><circle cx="12" cy="12" r="9" fill="none" stroke="#fff" stroke-width="2"/><path d="M3 12h18M12 3c3 3 3 15 0 18M12 3c-3 3-3 15 0 18" fill="none" stroke="#fff" stroke-width="1.6"/></svg>
      <span>www.marlowcrest-example.com.au</span>
    </div>
  </div>
</section>

</body>
</html>
```